Copper Lane Assembly - Crossroads Waltz CD Cover

To prepare a CD Cover for the single "Crossroads Waltz" by Copper Lane Assembly.
You can hear the single here:
http://copperlaneassembly.example/listen/

The CLA logo and backdrop are also provided if you want to incorporate them into the CD cover design, though that isn't mandatory.

Song is about deciding on taking on a serious relationship, and leaving the single life behind.

Target Market(s)

Music listeners, 18-50 yrs old, into retro 80s, Tin Orchards/Surf Monks

Industry/Entity Type

Music Download

Requirements
Must have
• CLA logo
• Crossroads Waltz title
Nice to have
• Use of backdrop, or facimile
Should not have
• Too obvious on the term Crossroads Waltz

```html
<!DOCTYPE html>
<html lang="en">
<head>
<meta charset="utf-8">
<title>Copper Lane Assembly – Crossroads Waltz</title>
<link rel="stylesheet" href="https://fonts.googleapis.com/css2?family=Antonio:wght@100;600&display=swap">
<style>
  :root {
    --frame: #000000;
    --navy-core: #073a5e;
    --navy-edge: #021d35;
    --neon-text: #c9ecea;
    --neon-glow: #38c6dc;
  }
  * { margin: 0; padding: 0; box-sizing: border-box; }
  html, body {
    width: 1200px;
    height: 1200px;
    overflow: hidden;
    background: var(--frame);
  }
  .cover {
    position: absolute;
    inset: 17px;
    background: radial-gradient(circle at 50% 50%, var(--navy-core) 0%, #053253 45%, var(--navy-edge) 100%);
    display: flex;
    flex-direction: column;
    align-items: center;
    font-family: "Antonio", "Arial Narrow", sans-serif;
    color: var(--neon-text);
  }
  .band-name {
    margin-top: 128px;
    font-weight: 600;
    font-size: 176px;
    line-height: 0.92;
    letter-spacing: 4px;
    text-align: center;
    text-transform: uppercase;
  }
  .band-name span { display: block; }
  .single-title {
    margin-top: 150px;
    font-weight: 100;
    font-size: 142px;
    line-height: 1;
    letter-spacing: 2px;
    text-transform: uppercase;
    white-space: nowrap;
    text-shadow:
      0 0 6px var(--neon-glow),
      0 0 16px var(--neon-glow),
      0 0 32px rgba(56, 198, 220, 0.6);
  }
</style>
</head>
<body>
  <main class="cover">
    <h1 class="band-name">
      <span>Copper</span>
      <span>Lane</span>
      <span>Assembly</span>
    </h1>
    <h2 class="single-title">Crossroads Waltz</h2>
  </main>
</body>
</html>
```